Lantern Business Cards

Need business cards for my employees at my restaurant.

Needs to include:
Our Logo
Lantern Bowls & Brews
Name: Nora Pettigrew
Title : Owner
Address: 487 Mirella Ave. Lake Havasu City, AZ 86519
Web: www.lanternkestrel.com
Phone: 928-555-0147
Cell: 928-555-0192
Email: info@lanternkestrel.com

```html
<!DOCTYPE html>
<html lang="en">
<head>
<meta charset="utf-8">
<title>Lantern Bowls &amp; Brews – Business Cards</title>
<link href="https://fonts.googleapis.com/css2?family=Poppins:wght@400;500;600;700&display=swap" rel="stylesheet">
<style>
  :root {
    --page-bg: #626365;
    --card-bg: #ececec;
    --brand-red: #b51d2e;
    --ink: #151515;
    --motif-red: #ead6d9;
    --motif-grey: #d9d9d9;
  }
  * { box-sizing: border-box; margin: 0; padding: 0; }
  html, body {
    width: 1200px; height: 900px; overflow: hidden;
    background: var(--page-bg);
    font-family: "Poppins", sans-serif;
  }
  .sheet {
    width: 1200px; height: 900px;
    display: flex; flex-direction: column; align-items: center; justify-content: center;
    gap: 34px;
  }
  .card {
    position: relative;
    width: 700px; height: 400px;
    background: var(--card-bg);
    overflow: hidden;
    box-shadow: 0 6px 14px rgba(0,0,0,0.28);
  }

  /* Brand lockup */
  .brand { display: flex; align-items: center; gap: 14px; }
  .brand-dot {
    width: 64px; height: 64px; border-radius: 50%;
    background: var(--brand-red);
    flex: none;
  }
  .brand-text { display: flex; flex-direction: column; align-items: center; }
  .brand-name {
    font-weight: 700; color: var(--brand-red);
    font-size: 46px; letter-spacing: 1px; text-transform: uppercase; line-height: 1;
  }
  .brand-tagline {
    font-weight: 700; color: var(--brand-red);
    font-size: 12px; letter-spacing: 2px; text-transform: uppercase; line-height: 1;
    margin-top: 6px;
  }

  /* Front */
  .card-front .brand { position: absolute; left: 44px; top: 52px; }
  .front-decoration {
    position: absolute; right: -70px; top: -30px;
    width: 300px; height: 460px;
    background: linear-gradient(135deg, var(--motif-red) 0%, var(--motif-grey) 100%);
    border-radius: 50% 0 0 50%;
    opacity: 0.75;
  }
  .person { position: absolute; left: 70px; top: 172px; }
  .person-name { font-size: 30px; font-weight: 600; color: var(--ink); line-height: 1.1; }
  .person-title { font-size: 17px; color: var(--brand-red); margin-top: 2px; }
  .contact-list {
    position: absolute; left: 84px; top: 258px;
    list-style: none; display: flex; flex-direction: column; gap: 9px;
  }
  .contact-item {
    display: flex; align-items: center; gap: 14px;
    font-size: 15px; font-weight: 500; color: var(--ink);
    white-space: nowrap;
  }
  .contact-icon { width: 16px; height: 16px; fill: var(--brand-red); flex: none; }

  /* Back */
  .back-pattern {
    position: absolute; inset: 0;
    background: linear-gradient(120deg, var(--motif-red) 0%, var(--motif-grey) 50%, var(--motif-red) 100%);
    opacity: 0.6;
  }
  .back-center {
    position: absolute; left: 50%; top: 50%; transform: translate(-50%, -50%);
    background: var(--card-bg);
    padding: 22px 40px;
  }
  .card-back .brand-name { font-size: 52px; }
  .card-back .brand-tagline { font-size: 14px; }
  .card-back .brand-dot { width: 80px; height: 80px; }
</style>
</head>
<body>
<main class="sheet">

  <section class="card card-front" aria-label="Business card front">
    <div class="front-decoration" role="img" aria-label="Large faint brand symbol in pale red and grey"></div>

    <div class="brand">
      <span class="brand-dot"></span>
      <div class="brand-text">
        <span class="brand-name">Lantern</span>
        <span class="brand-tagline">Bowls &amp; Brews</span>
      </div>
    </div>

    <div class="person">
      <p class="person-name">Nora Pettigrew</p>
      <p class="person-title">Owner</p>
    </div>

    <ul class="contact-list">
      <li class="contact-item">
        <svg class="contact-icon" viewBox="0 0 16 16"><path d="M8 0a5.5 5.5 0 0 0-5.5 5.5C2.5 10 8 16 8 16s5.5-6 5.5-10.5A5.5 5.5 0 0 0 8 0zm0 7.8a2.3 2.3 0 1 1 0-4.6 2.3 2.3 0 0 1 0 4.6z"/></svg>
        487 Mirella Ave. Lake Havasu City, AZ 86519
      </li>
      <li class="contact-item">
        <svg class="contact-icon" viewBox="0 0 16 16"><path d="M3.6 1l2.6 3-1.4 1.8c.9 2 2.4 3.5 4.4 4.4L11 8.8l3 2.6-1.6 2.8C6.7 14.5 1.5 9.3 1 3.6z"/></svg>
        928-555-0147 / 928-555-0192
      </li>
      <li class="contact-item">
        <svg class="contact-icon" viewBox="0 0 16 16"><path d="M1 3h14v10H1zm1.5 1.2L8 8.6l5.5-4.4z"/></svg>
        info@lanternkestrel.com
      </li>
      <li class="contact-item">
        <svg class="contact-icon" viewBox="0 0 16 16"><path d="M3 1l10 6-4.3 1 2.8 5.2-2 1L6.7 9 3 12z"/></svg>
        www.lanternkestrel.com
      </li>
    </ul>
  </section>

  <section class="card card-back" aria-label="Business card back">
    <div class="back-pattern" role="img" aria-label="Repeating faint brand symbol pattern in pale red and grey"></div>
    <div class="back-center">
      <div class="brand">
        <span class="brand-dot"></span>
        <div class="brand-text">
          <span class="brand-name">Lantern</span>
          <span class="brand-tagline">Bowls &amp; Brews</span>
        </div>
      </div>
    </div>
  </section>

</main>
</body>
</html>
```